Holloway-Prentiss & Associates
Business card & Word template design
Draft #12:
I like the shading -- it gives it dimension. But I would prefer a solid blue bar along the bottom (rather than a blue /black bar). I also like the back side of the bottom card. Could you remove the words "Financial Planning & Wealth Advisors" from the logo to make it look less busy?
Draft #10: Please see comments for Draft #11, as they apply as well. I like the wave on this one! One thought - could you put the phone and fax number on the same line to reduce the number of horizontal lines and create more balance for the long email address line?
Draft #11:
Nice work! I like the placement of the logo on the all-cap version (the design that has the logo on the left and more centered vertically). I like the shape of the all-cap letters but they seem lighter and not as easy to read(don't pop out as much as the other font). Could I please see a version that has the non-cap (darker) font on the layout with the logo on the left? Also, could you remove the word "email" from before the email address?
Draft #18 - additional note -- could you also please remove the comma after "Suite 485" in the address if it's on two different lines?
Draft #18:
Nice work! I like the blue area. I don't need the URL on the card, but I do need the words "Registered Investment Advisor" and "Financial Planning & Fee-Only Investments". Also, I like the line spacing on the address better than the line spacing on the phone/fax/email side of the card.
Nice work!
I am a little concerned with font being too small or narrow to be easily readable. I would like to see another font that has wider letters or perhaps the all-caps like the logo?
Also, I like to spell out "phone" and "fax" but not need an "e" or "email" for the email address.
Also, I would need the words "Registered Investment Advisor" and "Financial Planning & Fee-Only Investments" on the front (I'm looking for a single-sided card). If there's not enough space, can the words "Financial Planning and Wealth Advisors" be removed from the logo graphic to make more room?

```html
<!DOCTYPE html>
<html lang="en">
<head>
<meta charset="utf-8">
<title>Holloway-Prentiss &amp; Associates — Business Cards</title>
<link rel="stylesheet" href="https://fonts.googleapis.com/css2?family=Cinzel:wght@600&family=Open+Sans:wght@400;600;700&display=swap">
<style>
  :root {
    --bg: #ece9e4;
    --card-white: #ffffff;
    --card-shade: #e4e6e8;
    --brand-blue: #2f7fc8;
    --brand-blue-deep: #1f63a8;
    --brand-navy: #1d4f86;
    --text-white: #ffffff;
    --shadow: rgba(0,0,0,0.28);
  }
  * { box-sizing: border-box; margin: 0; padding: 0; }
  html, body { width: 1200px; height: 866px; overflow: hidden; }
  body { background: var(--bg); position: relative; font-family: "Open Sans", Arial, sans-serif; }

  .card {
    position: absolute;
    width: 352px;
    height: 204px;
    border-radius: 14px;
    overflow: hidden;
    box-shadow: 0 6px 16px var(--shadow);
  }
  .card__art { position: absolute; inset: 0; width: 100%; height: 100%; }

  /* Front */
  .card--front { left: 118px; top: 258px; background: linear-gradient(160deg, var(--card-white) 35%, var(--card-shade) 100%); }
  .front__brand {
    position: absolute; left: 24px; top: 28px;
    font-family: "Cinzel", Georgia, serif; font-weight: 600;
    color: var(--brand-navy); font-size: 15px; line-height: 1.25;
    display: flex; align-items: center; gap: 8px;
  }
  .front__brand-mark { width: 12px; height: 12px; background: var(--brand-blue); flex: none; }
  .front__credentials {
    position: absolute; left: 44px; top: 72px;
    color: var(--brand-blue-deep); font-size: 6.5px; font-weight: 600; line-height: 1.5;
  }
  .front__contact {
    position: absolute; right: 16px; top: 104px; width: 200px;
    text-align: right; color: var(--text-white); font-size: 6.5px; line-height: 1.45;
  }
  .front__name { font-size: 9px; font-weight: 700; }
  .front__role { font-size: 7px; margin-bottom: 4px; }
  .front__address { margin-bottom: 4px; line-height: 1.55; }

  /* Blue back */
  .card--back-blue { left: 630px; top: 190px; background: linear-gradient(180deg, var(--brand-blue) 0%, var(--brand-blue-deep) 100%); }
  /* White back */
  .card--back-white { left: 418px; top: 480px; background: linear-gradient(180deg, var(--card-white) 40%, var(--card-shade) 100%); }

  .back__brand {
    position: absolute; left: 0; right: 0; top: 62px; text-align: center;
    font-family: "Cinzel", Georgia, serif; font-weight: 600; font-size: 14px;
  }
  .back__tagline {
    position: absolute; left: 0; right: 0; top: 112px; text-align: center;
    font-size: 7.5px; font-weight: 600;
  }
  .card--back-blue .back__brand, .card--back-blue .back__tagline { color: var(--text-white); }
  .card--back-white .back__brand { color: var(--brand-navy); }
  .card--back-white .back__tagline { color: var(--brand-blue-deep); }
</style>
</head>
<body>

  <section class="card card--front" aria-label="Card front">
    <svg class="card__art" viewBox="0 0 352 204" preserveAspectRatio="none" aria-hidden="true">
      <defs>
        <linearGradient id="bandShade" x1="0" y1="0" x2="0" y2="1">
          <stop offset="0" stop-color="var(--brand-blue)"/>
          <stop offset="1" stop-color="var(--brand-blue-deep)"/>
        </linearGradient>
      </defs>
      <path d="M0 165 C 100 128, 210 100, 352 88 L 352 204 L 0 204 Z" fill="url(#bandShade)"/>
      <path d="M0 165 C 100 128, 210 100, 352 88" fill="none" stroke="rgba(255,255,255,0.35)" stroke-width="1.5"/>
    </svg>
    <div class="front__brand"><span class="front__brand-mark"></span><span>Holloway-Prentiss<br>&amp; Associates</span></div>
    <div class="front__credentials">
      <p>Registered Investment Advisor</p>
      <p>Financial Planning &amp; Fee-Only Investments</p>
    </div>
    <div class="front__contact">
      <p class="front__name">Marian Holloway-Prentiss</p>
      <p class="front__role">Principal</p>
      <p class="front__address">728 Alder Street, Suite 485<br>Cedar Vale, CA 95410</p>
      <p>Phone 555.210.4817 &nbsp;|&nbsp; Fax 555.210.4818</p>
      <p>marian@holloway-prentiss-associates.com</p>
    </div>
  </section>

  <section class="card card--back-blue" aria-label="Card back, blue">
    <svg class="card__art" viewBox="0 0 352 204" preserveAspectRatio="none" aria-hidden="true">
      <path d="M0 150 C 100 40, 250 40, 352 150" fill="none" stroke="rgba(255,255,255,0.18)" stroke-width="10"/>
      <path d="M0 204 L 0 160 C 100 60, 250 60, 352 160 L 352 204 Z" fill="rgba(255,255,255,0.05)"/>
    </svg>
    <p class="back__brand">Holloway-Prentiss &amp; Associates</p>
    <p class="back__tagline">Financial Planning &amp; Fee-Only Investments</p>
  </section>

  <section class="card card--back-white" aria-label="Card back, white">
    <svg class="card__art" viewBox="0 0 352 204" preserveAspectRatio="none" aria-hidden="true">
      <path d="M0 150 C 100 40, 250 40, 352 150" fill="none" stroke="rgba(0,0,0,0.05)" stroke-width="10"/>
      <path d="M0 204 L 0 160 C 100 60, 250 60, 352 160 L 352 204 Z" fill="rgba(0,0,0,0.03)"/>
    </svg>
    <p class="back__brand">Holloway-Prentiss &amp; Associates</p>
    <p class="back__tagline">Financial Planning &amp; Fee-Only Investments</p>
  </section>

</body>
</html>
```